Business Card for Luxury Hospitality Industry Career Seeker

Need something Simple, Punctual, and Elegant.

Project goal is to update phone number, layout, and wording

I look forward to working with you to create a business card I can give to managers and employers in the Luxury Hospitality industry. I want to advance a career in this industry handing out cards to managers and directors on my way up.
Updates

Updated graphics preferences in brief - would like my name flanked by small Lion, Compass, & Rope and have the Halworth 5 Star logo on the back Added Saturday, January 14, 2017

Updated Brief:-Some wording has been removed-Card Front should be more simple and tidy now-Card Back word choice & flow is improved Added Sunday, January 15, 2017

Target Market(s)

Luxury Hospitality Industry Employers and Managers

Industry/Entity Type

Hospitality

Contact Information for Business Card

(Card Front)
Corbin T. Pellman (flanked by small Lion, Compass & Rope graphic)
Luxury Hospitality
555-317-8846
ridgefellow@mailvessel.example
netroster.example/in/corbin-pellman-vet-civ
My Experience = Our Success

(Card Back)
Graphic of: Halworth 5 Star logo and maybe QTR 5 Diamond Logo too
8 years military supply, logistics, & administrative experience
2 years intensive recruiting, marketing, and sales expertise
Adept problem solving, planning and management skills
5 Star, 5 Daimond, Luxury Hotels & Hospitality Rooms & Revenue

Requirements
Must have
• Name
• Phone Number
• Email Address
• Net Roster Address
• Slogan (My Experience = Our Success)
• Graphic on back: Halworth 5 Star logo
• Qualification Remarks
• Catchy logo
Nice to have
• Background that makes a viewer think Luxury Hospitality Experience and/or World Experience
• Color combinations I've seen & liked are black & yellow, black & white, and blue & white

```html
<!DOCTYPE html>
<html lang="en">
<head>
<meta charset="utf-8">
<title>Corbin T. Pellman – Business Card</title>
<link rel="stylesheet" href="https://fonts.googleapis.com/css2?family=Cinzel:wght@600;700&family=Montserrat:wght@400;500&display=swap">
<style>
  :root {
    --stage: #2a2a2a;
    --card: #050505;
    --emblem-faint: #161616;
    --white: #f4f4f4;
    --yellow: #f2e21c;
    --gold: #b8975a;
    --badge-blue: #1f5bb8;
  }
  * { box-sizing: border-box; margin: 0; padding: 0; }
  html, body { width: 1200px; height: 900px; overflow: hidden; }
  body { background: var(--stage); position: relative; font-family: "Montserrat", sans-serif; }

  .card {
    position: absolute; left: 290px; width: 620px; height: 354px;
    background: var(--card); border-radius: 18px; overflow: hidden;
    box-shadow: 0 14px 30px rgba(0,0,0,.55);
  }
  .card--back { top: 60px; }
  .card--front { top: 480px; }

  .emblem-faint {
    position: absolute; border-radius: 50%;
    background: radial-gradient(circle, #1c1c1c 0%, var(--emblem-faint) 60%, rgba(20,20,20,0) 72%);
  }
  .card--back .emblem-faint { left: 230px; top: 40px; width: 260px; height: 260px; }
  .card--front .emblem-faint { left: 380px; top: -20px; width: 300px; height: 300px; }

  /* back */
  .rating-mark {
    position: absolute; left: 58px; top: 120px;
    display: flex; align-items: center; gap: 10px;
    font-family: "Cinzel", serif; font-weight: 700; font-size: 30px; color: var(--gold);
  }
  .rating-mark .dot { width: 14px; height: 14px; border-radius: 50%; background: var(--gold); }
  .award-badge { position: absolute; right: 60px; top: 28px; }
  .qualifications {
    position: absolute; left: 40px; top: 236px; list-style: none;
    color: var(--white); font-size: 14.5px; line-height: 23px;
  }
  .qualifications li { display: flex; align-items: center; gap: 8px; }
  .qualifications li::before {
    content: ""; width: 6px; height: 6px; border-radius: 50%; background: var(--yellow); flex: none;
  }

  /* front */
  .emblem-small {
    position: absolute; left: 372px; top: 70px; width: 70px; height: 70px;
    border-radius: 50%; background: radial-gradient(circle, #ffffff 0%, #bdbdbd 75%);
  }
  .identity { position: absolute; left: 50px; top: 100px; }
  .identity .name {
    font-family: "Cinzel", serif; font-weight: 700; font-size: 26px; letter-spacing: 2px;
    color: var(--white); padding-bottom: 8px; border-bottom: 2px solid var(--white); width: 330px;
  }
  .identity .role { color: var(--yellow); font-size: 15px; line-height: 22px; margin-top: 8px; }
  .contact-block {
    position: absolute; left: 36px; top: 210px; padding-left: 14px;
    border-left: 5px solid var(--white);
  }
  .contact-list { list-style: none; color: var(--white); font-size: 15px; line-height: 25px; }
  .contact-list li { display: flex; align-items: center; gap: 10px; }
  .contact-list svg { flex: none; }
  .network-dot { width: 10px; height: 10px; background: var(--yellow); flex: none; margin: 0 2px; }
  .slogan {
    font-family: "Cinzel", serif; font-weight: 700; font-size: 17px; letter-spacing: 1px;
    color: var(--yellow); margin-top: 6px;
  }
</style>
</head>
<body>

<section class="card card--back">
  <div class="emblem-faint" role="img" aria-label="Faint Lion, Compass & Rope emblem"></div>

  <svg class="award-badge" width="150" height="120" viewBox="0 0 150 120" role="img" aria-label="QTR 5 Diamond award badge">
    <polygon points="75,6 142,40 118,112 32,112 8,40" fill="var(--badge-blue)"/>
  </svg>

  <div class="rating-mark"><span class="dot"></span>Halworth</div>

  <ul class="qualifications">
    <li>8 years military supply, logistics, &amp; administrative experience</li>
    <li>2 years intensive recruiting, marketing, and sales expertise</li>
    <li>Adept problem solving, planning and management skills</li>
    <li>5 Star, 5 Daimond, Luxury Hotels &amp; Hospitality Rooms &amp; Revenue</li>
  </ul>
</section>

<section class="card card--front">
  <div class="emblem-faint" role="img" aria-label="Faint Lion, Compass & Rope emblem"></div>
  <div class="emblem-small" role="img" aria-label="Small Lion, Compass & Rope emblem"></div>

  <div class="identity">
    <h1 class="name">CORBIN T. PELLMAN</h1>
    <p class="role">Reservations Agent<br>Halworth 5 Star Luxury Hotel</p>
  </div>

  <div class="contact-block">
    <ul class="contact-list">
      <li>
        <svg width="14" height="14" viewBox="0 0 24 24"><path fill="var(--yellow)" d="M6.6 10.8a15 15 0 0 0 6.6 6.6l2.2-2.2a1 1 0 0 1 1-.25 11.4 11.4 0 0 0 3.6.57 1 1 0 0 1 1 1V20a1 1 0 0 1-1 1A17 17 0 0 1 3 4a1 1 0 0 1 1-1h3.5a1 1 0 0 1 1 1c0 1.25.2 2.45.57 3.57a1 1 0 0 1-.25 1z"/></svg>
        555-317-8846
      </li>
      <li>
        <svg width="14" height="14" viewBox="0 0 24 24"><rect x="2.5" y="5" width="19" height="14" rx="1.5" fill="none" stroke="var(--yellow)" stroke-width="2.4"/><path d="M3 6l9 7 9-7" fill="none" stroke="var(--yellow)" stroke-width="2.4"/></svg>
        ridgefellow@mailvessel.example
      </li>
      <li><span class="network-dot"></span>netroster.example/in/corbin-pellman-vet-civ</li>
    </ul>
    <p class="slogan">MY EXPERIENCE = OUR SUCCESS</p>
  </div>
</section>

</body>
</html>
```